My name is Tomas Verenda, and I have done business with your company several times. I need a business card to represent my business, I own a company by the name of BELOMI Suntan Lotion & Sunscreen.
My requirements are as follow: My company logo in the brightest gold possible, on a black, grainy (sandy) background, with shading around the each element. With the company name in gold, a stylized coconut trees, and some type of wave graphic in gold. "A product of the USA, Marlow Bay, ME"
"For comments, suggestion, or ordering please contact us at:
belomi42@nexamail.test"

"BELOMI™ Tanning Lotion & Sunscreen―Crafted with Care"

Belomi Tanning Lotion & Sunscreen is the most extraordinary and innovative sun tanning product to emerge in several generations. The constituents of this product are formidable substances that protect the skin against the aftermath of sun exposure−before you exposed yourself to the sun’s rays. The Aloe Vera in this product, along with other oils and cream, are specifically manufactured to lessen the symptoms of extended exposure to the sun. Belomi is designed to provide a Broad Spectrum Protection (50) that assist in the reduction of (UVA) and (UVB) radiation to create a magnificent sun-absorbing, long-lasting, deep dark bronzing experience.
Thank you,
Tomas Verenda
tomastverenda@postline.test

Target Market(s)

Sunscreen

Industry/Entity Type

Business

Contact Information for Business Card

BELOMI™ Tanning Lotion and Sunscreen
Crafted with Care

Belomi Tanning Lotion is the most extraordinary and innovative sun tanning product to emerge in several generations. The constituents of this product are formidable substances that protect the skin against the aftermath of sun exposure−before you exposed yourself to the sun’s rays. The Aloe Vera, in this product, along with other oils and cream, are specifically manufactured to lessen the symptoms of extended exposure to the sun. Belomi protects your skin from dehydration and treat your skin with the products we apply to ourselves after a sunburn−before the sun tanning process begins. Belomi is designed to provide a Broad Spectrum Protection (50) that assist in the reduction of (UVA) and (UVB) radiation to create a magnificent sun-absorbing, long-lasting, deep dark bronzing experience.

Colors
fece3e
acd136

Requirements
Must have
• Black Card Stock with grainy surface, Gold Logo, stylized Coconut Palm Tree, Company Name, email address, and NYC location.
• Modern Layout with Modern fonts and graphics

```html
<!DOCTYPE html>
<html lang="en">
<head>
<meta charset="utf-8">
<title>Belomi Business Card</title>
<link href="https://fonts.googleapis.com/css2?family=Cinzel:wght@600&family=Open+Sans:wght@400;600;700&family=Roboto+Slab:wght@800&display=swap" rel="stylesheet">
<style>
  :root {
    --stage: #8f8f8f;
    --card: #141414;
    --gold: #c9a45c;
    --gold-bright: #f2d675;
    --gold-deep: #6e3c16;
    --gold-mid: #b8862e;
    --role-gold: #d8b23c;
    --text-light: #e2e2e2;
    --icon: #cfcfcf;
    --white: #ffffff;
    --divider: #5a5a5a;
    --tag-rule: #d38a2e;
  }
  * { margin: 0; padding: 0; box-sizing: border-box; }
  html, body { width: 1105px; height: 1200px; overflow: hidden; }
  body { background: var(--stage); position: relative; font-family: "Open Sans", sans-serif; }

  .card {
    position: absolute;
    left: 196px;
    width: 721px;
    background:
      radial-gradient(circle at 30% 40%, rgba(255,255,255,0.035) 0, transparent 60%),
      repeating-radial-gradient(circle at 0 0, rgba(255,255,255,0.025) 0 1px, transparent 1px 3px),
      var(--card);
    box-shadow: 4px 6px 10px rgba(0,0,0,0.45);
    overflow: hidden;
  }
  .card--front { top: 145px; height: 413px; }
  .card--back { top: 602px; height: 410px; }

  .brand-mark {
    position: absolute;
    border-radius: 50%;
    background: radial-gradient(circle at 40% 35%, var(--gold-bright), var(--gold-mid) 60%, var(--gold-deep));
  }
  .brand-name {
    position: absolute;
    font-family: "Cinzel", serif;
    font-weight: 600;
    color: var(--gold);
    letter-spacing: 1px;
    line-height: 1;
    white-space: nowrap;
  }

  /* Front */
  .card--front .brand-mark { left: 166px; top: 120px; width: 90px; height: 90px; }
  .card--front .brand-name { left: 100px; width: 222px; text-align: center; top: 226px; font-size: 44px; }
  .brand-descriptor {
    position: absolute; left: 100px; width: 222px; top: 272px;
    text-align: center; font-size: 18px; line-height: 1; color: var(--gold); letter-spacing: 0.5px;
  }
  .divider {
    position: absolute; left: 374px; top: 110px; width: 1px; height: 187px;
    background: linear-gradient(transparent, var(--divider) 20%, var(--divider) 80%, transparent);
  }
  .contact { position: absolute; left: 421px; top: 124px; }
  .contact__name { font-size: 25px; font-weight: 700; color: var(--gold); letter-spacing: 0.5px; line-height: 1.2; }
  .contact__role { font-size: 19px; font-weight: 600; color: var(--role-gold); margin-bottom: 14px; }
  .contact__line { display: flex; align-items: center; gap: 10px; font-size: 18px; color: var(--text-light); height: 27px; }
  .contact__line svg { width: 16px; height: 16px; fill: var(--icon); flex: none; }

  .gold-band {
    position: absolute; left: 0; bottom: 0; width: 100%; height: 32px;
    background: linear-gradient(90deg, var(--gold-deep), var(--gold-mid) 30%, var(--gold-bright) 50%, var(--gold-mid) 70%, var(--gold-deep));
  }
  .gold-rule {
    position: absolute; left: 0; bottom: 35px; width: 100%; height: 2px;
    background: linear-gradient(90deg, var(--gold-deep), var(--gold-bright) 50%, var(--gold-deep));
  }

  /* Back */
  .card--back .brand-mark { left: 145px; top: 134px; width: 102px; height: 102px; }
  .card--back .brand-name { left: 262px; top: 124px; font-size: 48px; color: var(--white); }
  .card--back .brand-name sup { font-family: "Open Sans", sans-serif; font-size: 16px; vertical-align: top; position: relative; top: 2px; margin-left: 4px; }
  .tag-rule { position: absolute; left: 262px; top: 196px; width: 287px; height: 3px; background: var(--tag-rule); }
  .tagline {
    position: absolute; left: 262px; top: 201px; white-space: nowrap;
    font-family: "Roboto Slab", serif; font-weight: 800; font-size: 18px; color: var(--white);
  }
  .origin {
    position: absolute; left: 0; width: 100%; top: 295px; text-align: center;
    font-size: 18px; line-height: 25px; color: var(--white);
  }
  .origin__email { font-weight: 700; font-size: 20px; }
</style>
</head>
<body>

<section class="card card--front">
  <div class="brand-mark"></div>
  <div class="brand-name">BELOMI</div>
  <div class="brand-descriptor">SUNTAN LOTION</div>

  <div class="divider"></div>

  <div class="contact">
    <div class="contact__name">DANA MORROW</div>
    <div class="contact__role">CEO/Founder</div>
    <div class="contact__line">
      <svg viewBox="0 0 16 16"><path d="M3.5 1 6 1.6 6.8 5 5.2 6.3c.9 1.9 2.5 3.5 4.5 4.5L11 9.2l3.4.8.6 2.5-1.8 2C7.4 14.2 1.8 8.6 1.5 2.8z"/></svg>
      <span>555 014 7720</span>
    </div>
    <div class="contact__line">
      <svg viewBox="0 0 16 16"><path d="M4 0h8a1 1 0 0 1 1 1v14a1 1 0 0 1-1 1H4a1 1 0 0 1-1-1V1a1 1 0 0 1 1-1zm1 2v10h6V2zm3 11a1 1 0 1 0 0 2 1 1 0 0 0 0-2z"/></svg>
      <span>555 019 3184</span>
    </div>
    <div class="contact__line">
      <svg viewBox="0 0 16 16"><path d="M8 0a8 8 0 1 0 0 16A8 8 0 0 0 8 0zm-1 2.2c-.6 1-.2 2 .8 2.3 1 .3.4 1.6-.6 1.8-1 .2-1.8.9-1.4 2 .4 1 1.6.9 2.2 1.9.5 1-.1 2.5.6 3.4A6 6 0 0 1 2.2 6.3c.9.2 1.8-.3 2.2-1.2C4.9 4 6 3 7 2.2zm3.2.4A6 6 0 0 1 14 8c-.8-.3-1.5.2-2 .9-.6-1-2.3-1-2.2-2.4.1-1 1.1-1 1.3-2 .1-.7-.4-1.3-.9-1.9z"/></svg>
      <span>www.belomi.test</span>
    </div>
  </div>

  <div class="gold-rule"></div>
  <div class="gold-band"></div>
</section>

<section class="card card--back">
  <div class="brand-mark"></div>
  <div class="brand-name">BELOMI<sup>TM</sup></div>
  <div class="tag-rule"></div>
  <div class="tagline">Tanning Lotion-Crafted with Care</div>

  <p class="origin">
    A product of the USA, Marlow Bay, ME<br>
    For comments, suggestion, or ordering please contact us at:<br>
    <span class="origin__email">belomi42@nexamail.test</span>
  </p>
</section>

</body>
</html>
```